Flyer-Design für Schwimmtraining für Triathleten
Zielgruppe
Angebot
Schwimmen: als Personal Training, in Kleingruppen oder im Kraulkurs
Schwimmen: Videoanalysen
Triathlon: Trainingspläne, Leistungsdiagnostik
Zielgruppe des Flyers:
Triathleten jeder Leistungsklasse
Flyer ist a) als Auslage in Sportgeschäften, b) als Beilage in Wettkampftüten von Triathlonwettkämpfen gedacht
Aufgabenstellung
Triathleten sind tendenziell technisch orientierte Menschen, vergleichsweise wohlhabend. Schwimmen ist häufig eher die verhasste aber notwendige Teil der drei Disziplinen.
Bitte kein Standardformat für den Flyer.
Die Herausforderung bei einem Flyer als Beigabe zum Wettkampfbeutel: Überlicherweise wird der ganze Packen Werbung achtlos weggeworfen. Design und Format sollen dazu beitragen, dass der Flyer heraussticht und möglichst beachtet wird.
Grundsätzliche Infos: www.kelbrun42.de

```html
<!DOCTYPE html>
<html lang="de">
<head>
<meta charset="utf-8">
<title>Schwimmtraining Flyer</title>
<link href="https://fonts.googleapis.com/css2?family=Didact+Gothic&family=Questrial&display=swap" rel="stylesheet">
<style>
  :root {
    --stage: #a9bcba;
    --ink: #021820;
    --ice: #e8fbfd;
    --aqua: #45c0ef;
    --ring: #2f444c;
    --white: #ffffff;
    --photo-top: #9fb3a8;
    --photo-mid: #6f7f6a;
    --photo-low: #3d3a2c;
  }
  html, body {
    margin: 0;
    width: 1200px;
    height: 649px;
    overflow: hidden;
    background: var(--stage);
  }
  .flyer-frame {
    position: absolute;
    left: 363px;
    top: 20px;
    width: 474px;
    height: 609px;
    box-shadow: 0 8px 24px rgba(0,0,0,.35);
  }
  .flyer {
    position: absolute;
    left: 0; top: 0;
    width: 800px;
    height: 1028px;
    transform: scale(0.5925);
    transform-origin: 0 0;
    background: var(--ink);
    font-family: "Didact Gothic", "Questrial", sans-serif;
    color: var(--white);
    overflow: hidden;
  }
  .flyer-shapes { position: absolute; left: 0; top: 0; }
  .offer-badge {
    position: absolute;
    left: 85px; top: 120px;
    width: 150px; height: 150px;
    text-align: center;
  }
  .offer-badge .offer-label { margin-top: 20px; font-size: 19px; letter-spacing: .5px; }
  .offer-badge .offer-value { font-size: 30px; color: var(--aqua); line-height: 1.1; }
  .offer-badge .offer-note { font-size: 12px; line-height: 1.3; margin-top: 8px; }
  .headline {
    position: absolute;
    left: 500px; top: 393px;
    width: 240px;
    text-align: center;
    font-family: "Questrial", sans-serif;
    font-size: 36px;
    line-height: 42px;
    color: var(--ink);
  }
  .headline .accent { color: var(--aqua); }
  .service {
    position: absolute;
    left: 86px;
    width: 400px;
  }
  .service h2 {
    margin: 0 0 4px;
    font-weight: 400;
    font-size: 26px;
    color: var(--aqua);
  }
  .service p { margin: 0; font-size: 14.5px; line-height: 18.5px; }
  .service-personal { top: 472px; }
  .service-programs { top: 576px; left: 89px; }
  .service-analysis { top: 681px; left: 89px; }
  .step-number {
    position: absolute;
    width: 80px;
    text-align: center;
    font-family: "Questrial", sans-serif;
    font-size: 38px;
    color: var(--aqua);
  }
  .brand-block {
    position: absolute;
    left: 472px; top: 872px;
    width: 266px; height: 110px;
    display: flex;
    align-items: center;
    justify-content: center;
    font-size: 36px;
    letter-spacing: 1px;
    color: var(--white);
  }
  .website {
    position: absolute;
    left: 95px; top: 973px;
    font-size: 14px;
  }
</style>
</head>
<body>
<div class="flyer-frame">
  <div class="flyer">
    <svg class="flyer-shapes" width="800" height="1028" viewBox="0 0 800 1028">
      <defs>
        <linearGradient id="water" x1="0" y1="0" x2="0" y2="1">
          <stop offset="0" stop-color="var(--photo-top)"/>
          <stop offset=".6" stop-color="var(--photo-mid)"/>
          <stop offset="1" stop-color="var(--photo-low)"/>
        </linearGradient>
      </defs>
      <polygon class="corner-light" points="0,0 365,0 169,180" fill="var(--ice)"/>
      <polygon class="photo-area" role="img" aria-label="Foto: lächelnder Schwimmer mit Badekappe und Schwimmbrille im Wasser"
               points="365,0 800,0 800,75 418,446 169,180" fill="url(#water)"/>
      <polygon class="stripe" points="355,0 368,0 218,140 205,133" fill="var(--aqua)"/>
      <polygon class="stripe" points="800,68 800,84 426,454 414,442" fill="var(--aqua)"/>
      <polygon class="panel-light" points="800,92 800,853 428,456" fill="var(--ice)"/>
      <circle class="offer-ring" cx="160" cy="195" r="75" fill="var(--ink)" stroke="var(--ice)" stroke-width="5"/>
      <circle class="step-dot" cx="478" cy="520" r="44" fill="var(--ice)" stroke="var(--ring)" stroke-width="8"/>
      <circle class="step-dot" cx="578" cy="623" r="44" fill="var(--ice)" stroke="var(--ring)" stroke-width="8"/>
      <circle class="step-dot" cx="683" cy="730" r="44" fill="var(--ice)" stroke="var(--ring)" stroke-width="8"/>
    </svg>

    <div class="offer-badge">
      <div class="offer-label">ANGEBOT</div>
      <div class="offer-value">50%</div>
      <div class="offer-note">Rabatt auf Ihre<br>erste Trainings-Stunde</div>
    </div>

    <div class="headline">SPORT IS A<br>PRESERVER<br>OF <span class="accent">HEALTH</span></div>

    <span class="step-number" style="left:438px;top:496px;">1</span>
    <span class="step-number" style="left:536px;top:598px;">2</span>
    <span class="step-number" style="left:642px;top:706px;">3</span>

    <section class="service service-personal">
      <h2>Personal Training</h2>
      <p>Steigern Sie Ihre Schwimmkünste mit<br>einem persönlichem Trainer!<br>Alleine oder in Kleingruppen.</p>
    </section>
    <section class="service service-programs">
      <h2>Sport Programs</h2>
      <p>Wir erstellen Tainingspläne ganz auf Ihrer<br>Bedürfnisse angepasst.</p>
    </section>
    <section class="service service-analysis">
      <h2>Analysen und mehr...</h2>
      <p>Durch Videoanalysen kontrollieren wir Ihren Fortschritt<br>und passen somit Ihren Traininsplan an.</p>
    </section>

    <div class="brand-block">KELBRUN42</div>
    <div class="website">www.kelbrun42.de</div>
  </div>
</div>
</body>
</html>
```